Business Card Design

We need two business cards - same design but with two different people's details.

We are a new start-up online cleaning business that allows people to book and pay for a quality home cleaner online.

We would like a professional yet overly formal style of business card.

Target Market(s)

18 - 65+ professionals

Industry/Entity Type

Business

Contact Information for Business Card

We would like two business cards but with the same design, the details are below:

Peter Valdoro
Director and Co-Founder
ph: 0421 573 916
Suite 3C, Level 4
517 Harwood Road
Belmira NSW 2089
peter@tidlo.com.au

_______________________________________________________

Evangelia Valdoro
Director and Co-Founder
ph: 0432 915047
Suite 3C, Level 4
517 Harwood Road
Belmira NSW 2089
evangelia@tidlo.com.au

Requirements
Must have
• although our style guide refers to orange and red, please stick to the blue/black/grey that is in the style guide.

also on the back of the card we would like the logo with our tag line which is on page 12 of the style guide.
Should not have
• no pictures of mops, cleaners etc

```html
<!DOCTYPE html>
<html lang="en">
<head>
<meta charset="utf-8">
<title>Tidlo business card</title>
<link rel="stylesheet" href="https://fonts.googleapis.com/css2?family=Quicksand:wght@300;400;500;700&display=swap">
<style>
  :root {
    --page: #e9ecef;
    --card-white: #f7f8f9;
    --card-grey: #e4e6e8;
    --brand-blue: #4fb3de;
    --brand-blue-light: #8fd3ef;
    --brand-blue-deep: #2f97c6;
    --ink: #3a3d40;
    --ink-soft: #8a8e92;
    --faint: #dcdfe2;
  }
  * { box-sizing: border-box; margin: 0; padding: 0; }
  html, body { width: 1200px; height: 1023px; overflow: hidden; }
  body {
    background: var(--page);
    font-family: "Quicksand", sans-serif;
    color: var(--ink);
    position: relative;
  }
  .card {
    position: absolute;
    width: 540px;
    height: 330px;
    border-radius: 4px;
    overflow: hidden;
    box-shadow: 0 6px 18px rgba(0,0,0,.12);
  }
  .card--front { left: 40px; top: 346px; background: var(--card-white); }
  .card--back {
    left: 620px; top: 346px;
    background: linear-gradient(135deg, #ffffff 0%, var(--card-white) 45%, var(--card-grey) 100%);
  }
  .card__waves { position: absolute; inset: 0; }

  /* Front */
  .front-brand {
    position: absolute;
    left: 90px; top: 112px;
    display: flex; align-items: center; gap: 16px;
  }
  .brand-dot {
    width: 58px; height: 58px; border-radius: 50%;
    background: var(--brand-blue);
    flex: none;
  }
  .brand-name {
    font-weight: 700;
    font-size: 62px;
    line-height: 1;
    color: var(--ink);
    letter-spacing: -1px;
  }
  .front-tagline {
    position: absolute;
    left: 164px; top: 182px;
    font-size: 15px; font-weight: 400;
    color: var(--ink);
    white-space: nowrap;
  }

  /* Back */
  .back-decor {
    position: absolute;
    left: -80px; top: 112px;
    width: 260px; height: 260px; border-radius: 50%;
    border: 34px solid var(--faint);
  }
  .back-brand {
    position: absolute;
    left: 28px; top: 24px;
    display: flex; align-items: center; gap: 12px;
  }
  .back-brand .brand-dot { width: 44px; height: 44px; }
  .back-brand .brand-name { font-size: 50px; }
  .back-tagline {
    position: absolute;
    left: 86px; top: 82px;
    font-size: 12.5px; color: var(--ink);
    white-space: nowrap;
  }
  .contact {
    position: absolute;
    right: 24px; bottom: 22px;
    width: 290px;
  }
  .contact__name {
    font-size: 22px; font-weight: 500;
    color: var(--brand-blue);
    line-height: 1.1;
  }
  .contact__role {
    font-size: 11.5px; font-weight: 700; color: var(--ink);
    margin-top: 2px;
  }
  .contact__rule {
    border: 0; border-top: 1px dashed #b9bdc1;
    margin: 8px 0 10px;
  }
  .contact__row {
    display: flex; justify-content: space-between; align-items: center;
    gap: 12px;
    margin-bottom: 8px;
  }
  .contact__row:last-child { margin-bottom: 0; }
  .contact__text {
    font-size: 12px; font-weight: 300; color: var(--ink-soft);
    line-height: 1.35;
  }
  .contact__icon {
    width: 24px; height: 24px; flex: none;
    background: var(--brand-blue); border-radius: 4px;
    display: flex; align-items: center; justify-content: center;
  }
  .contact__icon svg { width: 14px; height: 14px; }
</style>
</head>
<body>

  <section class="card card--front" aria-label="Card front">
    <svg class="card__waves" viewBox="0 0 540 330" preserveAspectRatio="none" aria-hidden="true">
      <defs>
        <linearGradient id="bandTop" x1="0" y1="0" x2="1" y2="1">
          <stop offset="0" stop-color="#8fd3ef"/>
          <stop offset="1" stop-color="#4fb3de"/>
        </linearGradient>
        <linearGradient id="bandBottom" x1="0" y1="0" x2="1" y2="1">
          <stop offset="0" stop-color="#4fb3de"/>
          <stop offset="1" stop-color="#2f97c6"/>
        </linearGradient>
      </defs>
      <path d="M0 0 H540 V0 C420 20 300 60 190 80 C110 94 40 94 0 84 Z" fill="url(#bandTop)"/>
      <path d="M540 150 C490 200 440 250 370 292 C320 320 270 330 230 330 H540 Z" fill="url(#bandBottom)"/>
      <path d="M540 150 C490 200 440 250 370 292 C320 320 270 330 230 330" fill="none" stroke="#9aa3a9" stroke-opacity=".35" stroke-width="3"/>
    </svg>
    <div class="front-brand">
      <span class="brand-dot"></span>
      <span class="brand-name">Tidlo</span>
    </div>
    <p class="front-tagline">Spotless homes, booked in minutes</p>
  </section>

  <section class="card card--back" aria-label="Card back">
    <div class="back-decor" aria-hidden="true"></div>
    <div class="back-brand">
      <span class="brand-dot"></span>
      <span class="brand-name">Tidlo</span>
    </div>
    <p class="back-tagline">Spotless homes, booked in minutes</p>

    <div class="contact">
      <p class="contact__name">Peter Valdoro</p>
      <p class="contact__role">Director and Co-Founder</p>
      <hr class="contact__rule">
      <div class="contact__row">
        <p class="contact__text">ph: 0421 573 916</p>
        <span class="contact__icon">
          <svg viewBox="0 0 24 24" aria-label="Phone"><path fill="#fff" d="M6.6 10.8a15.1 15.1 0 0 0 6.6 6.6l2.2-2.2a1 1 0 0 1 1-.25 11.4 11.4 0 0 0 3.6.57 1 1 0 0 1 1 1V20a1 1 0 0 1-1 1A17 17 0 0 1 3 4a1 1 0 0 1 1-1h3.5a1 1 0 0 1 1 1c0 1.25.2 2.45.57 3.57a1 1 0 0 1-.25 1z"/></svg>
        </span>
      </div>
      <div class="contact__row">
        <p class="contact__text">Suite 3C, Level 4, 517 Harwood Road<br>Belmira NSW 2089</p>
        <span class="contact__icon">
          <svg viewBox="0 0 24 24" aria-label="Address"><path fill="#fff" d="M12 2a7 7 0 0 0-7 7c0 5.2 7 13 7 13s7-7.8 7-13a7 7 0 0 0-7-7zm0 9.5A2.5 2.5 0 1 1 12 6.5a2.5 2.5 0 0 1 0 5z"/></svg>
        </span>
      </div>
      <div class="contact__row">
        <p class="contact__text">peter@tidlo.com.au</p>
        <span class="contact__icon">
          <svg viewBox="0 0 24 24" aria-label="Email"><path fill="none" stroke="#fff" stroke-width="2" d="M3 6h18v12H3z M3 6l9 7 9-7"/></svg>
        </span>
      </div>
    </div>
  </section>

</body>
</html>
```